Banner poster with different motifs

I'm looking for 5 banners and posters in A1 format in the same design, or the similarity must be recognizable...
Kept quite simple with different titles.

1 ballet
2 Contemporary Dance
3 high heels
4 Salsa & Bachata & Zouk
5 Hip Hop

Modern bright colors
it is for the entrance so that the students see here is a dance school

The text may also be included in the image
The photos are for guidance only; some are our own, some are purchased. However, we are permitted to use them, including our logo, of course.

```html
<!DOCTYPE html>
<html lang="en">
<head>
<meta charset="utf-8">
<title>Ballet – Veloria Dance Center</title>
<link rel="stylesheet" href="https://fonts.googleapis.com/css2?family=Anton&family=Montserrat:wght@300;400;500&display=swap">
<style>
  :root {
    --magenta-glow: #c8307f;
    --magenta-mid: #a81a62;
    --magenta-deep: #8c0f48;
    --white: #ffffff;
    --photo-light: #f4e6ec;
    --photo-soft: #e9c6d6;
  }
  * { margin: 0; padding: 0; box-sizing: border-box; }
  html, body {
    width: 849px;
    height: 1200px;
    overflow: hidden;
    background: var(--magenta-deep);
  }
  .poster {
    position: relative;
    width: 849px;
    height: 1200px;
    overflow: hidden;
    background: radial-gradient(ellipse 62% 48% at 48% 46%, var(--magenta-glow) 0%, var(--magenta-mid) 55%, var(--magenta-deep) 100%);
  }
  .brand {
    position: absolute;
    top: 82px;
    left: 0;
    width: 100%;
    text-align: center;
    color: var(--white);
    font-family: "Montserrat", sans-serif;
  }
  .brand-circle {
    display: block;
    width: 90px;
    height: 90px;
    margin: 0 auto;
    border: 2px solid var(--white);
    border-radius: 50%;
  }
  .brand-name {
    margin-top: 18px;
    font-size: 42px;
    font-weight: 300;
    letter-spacing: 4px;
    line-height: 1;
  }
  .brand-tagline {
    margin-top: 8px;
    font-size: 14px;
    font-weight: 400;
    letter-spacing: 2.6px;
    line-height: 1;
  }
  .title-art {
    position: absolute;
    left: 0;
    top: 0;
    width: 849px;
    height: 1200px;
  }
  .title-word {
    font-family: "Anton", sans-serif;
    fill: var(--white);
  }
</style>
</head>
<body>
  <main class="poster">
    <header class="brand">
      <span class="brand-circle"></span>
      <p class="brand-name">VELORIA</p>
      <p class="brand-tagline">DANCE CENTER RIVERSIDE</p>
    </header>

    <svg class="title-art" viewBox="0 0 849 1200" aria-hidden="false">
      <defs>
        <radialGradient id="dancer-tone" cx="50%" cy="50%" r="50%">
          <stop offset="0%" stop-color="var(--photo-light)" stop-opacity="0.55"/>
          <stop offset="60%" stop-color="var(--photo-soft)" stop-opacity="0.25"/>
          <stop offset="100%" stop-color="var(--photo-soft)" stop-opacity="0"/>
        </radialGradient>
      </defs>

      <g transform="translate(290 292) rotate(90)">
        <text class="title-word" x="0" y="0" font-size="368" textLength="808" lengthAdjust="spacingAndGlyphs">BALLET</text>
      </g>

      <ellipse cx="420" cy="720" rx="250" ry="420" fill="url(#dancer-tone)"
               role="img" aria-label="Photo of a ballerina in a white tutu on pointe, one arm raised, posing in front of the title"/>
    </svg>
  </main>
</body>
</html>
```